varnuko.com car care product labeling with cut outs will be printed on holographic sheet.

Need to make label for eco-friendly car care products. no hazard signs.
clean and simple design minimalism
wheel cleaner
tire shiner
glass cleaner
all purpose cleaner
247x90mm
166x150mm

Target Market(s)

eco friendly car care products. europe , uae

Industry/Entity Type

car care products, eco-friendly product line

Requirements
Must have
• BW design print on holographic sheet/label .eco-friendly signs
Nice to have
• premium product look and simplicity will be at first place, can be with cut outs

```html
<!DOCTYPE html>
<html lang="en">
<head>
<meta charset="utf-8">
<title>varnuko Wheel Cleaner Label</title>
<link href="https://fonts.googleapis.com/css2?family=Montserrat:wght@300;400;700&display=swap" rel="stylesheet">
<style>
  :root {
    --page: #eceeef;
    --silver-light: #e4e8ea;
    --silver-mid: #c3c9cc;
    --silver-dark: #a9b1b5;
    --ink: #111111;
    --wheel-tone: #aab4ba;
    --green-deep: #0b6a22;
    --green-bright: #22a63c;
    --badge-ring: #57b848;
  }
  html, body {
    margin: 0;
    padding: 0;
    width: 1200px;
    height: 1200px;
    overflow: hidden;
    background: var(--page);
  }
  .label {
    position: absolute;
    left: 50px;
    top: 400px;
    width: 1100px;
    height: 400px;
    overflow: hidden;
    background: linear-gradient(115deg, var(--silver-dark) 0%, var(--silver-light) 28%, var(--silver-mid) 46%, var(--silver-light) 62%, var(--silver-dark) 84%, var(--silver-mid) 100%);
    font-family: "Montserrat", sans-serif;
    color: var(--ink);
  }
  .wheel-graphic {
    position: absolute;
    left: -60px;
    top: 130px;
    width: 380px;
    height: 380px;
    border-radius: 50%;
    background: radial-gradient(circle, var(--silver-mid) 0%, var(--wheel-tone) 60%, rgba(170,180,186,0.4) 100%);
  }
  .brand {
    position: absolute;
    left: 380px;
    top: 28px;
    margin: 0;
    font-weight: 700;
    font-size: 84px;
    letter-spacing: -1px;
    line-height: 1;
  }
  .product-name {
    position: absolute;
    left: 400px;
    top: 170px;
    margin: 0;
    font-weight: 300;
    font-size: 54px;
    line-height: 1.05;
    letter-spacing: 1px;
  }
  .brush-stroke {
    position: absolute;
    left: 400px;
    top: 302px;
    width: 300px;
    height: 16px;
    border-radius: 2px 8px 8px 2px;
    background: linear-gradient(90deg, rgba(17,17,17,0) 0%, rgba(17,17,17,0.6) 30%, var(--ink) 55%);
  }
  .volume {
    position: absolute;
    left: 520px;
    top: 352px;
    margin: 0;
    font-weight: 400;
    font-size: 20px;
  }
  .volume .estimated {
    font-weight: 700;
    font-size: 26px;
    margin-left: 6px;
  }
  .eco-band {
    position: absolute;
    left: 920px;
    top: 0;
    width: 46px;
    height: 400px;
    background: linear-gradient(160deg, var(--green-deep) 0%, var(--green-bright) 30%, #063d14 50%, var(--green-bright) 70%, var(--green-deep) 100%);
  }
  .eco-badge {
    position: absolute;
    left: 862px;
    top: 238px;
  }
</style>
</head>
<body>
  <section class="label">
    <div class="wheel-graphic" role="img" aria-label="Large faint silver alloy wheel illustration"></div>
    <h1 class="brand">varnuko</h1>
    <h2 class="product-name">WHEEL<br>CLEANER</h2>
    <div class="brush-stroke" role="img" aria-label="Black brush stroke underline"></div>
    <p class="volume">500ml<span class="estimated">℮</span></p>
    <div class="eco-band"></div>
    <svg class="eco-badge" width="150" height="150" viewBox="0 0 150 150" aria-hidden="true">
      <circle cx="75" cy="75" r="70" fill="#ffffff" stroke="var(--badge-ring)" stroke-width="5"/>
      <circle cx="75" cy="75" r="38" fill="var(--green-deep)"/>
    </svg>
  </section>
</body>
</html>
```